World Wide News and Current Affairs website

We intends to start up a new website which deals on New and Current Affairs.
Attention Designers,
We want a home page design for this project. Our business is based in the United States. Our goal is to become a well known brand.
The website would consist of a category for News, Business and Tech.
The theme should be beautiful and attention seeking. The website would take bulk of it's news from the US, and Europe.
Designers can get inspiration from already existing new websites such as HVZ, FQJ, DORNAKE.
All designs should be clean and easy to navigate.

```html
<!DOCTYPE html>
<html lang="en">
<head>
<meta charset="utf-8">
<title>News Home</title>
<link rel="stylesheet" href="https://fonts.googleapis.com/css2?family=Hind:wght@400;500;600;700&family=Cabin:wght@400;500;600&family=Arimo:wght@400&display=swap">
<style>
:root{
  --brand:#0a5fa8;
  --nav:#2f2f2f;
  --page:#e6e6e6;
  --panel:#ffffff;
  --wire-bg:#f4f4f4;
  --ink:#222;
  --muted:#8a8a8a;
  --footer:#b4b4b4;
  --footer-ink:#333;
}
*{box-sizing:border-box;margin:0;padding:0}
html,body{width:1200px;height:1000px;overflow:hidden}
body{background:var(--page);font-family:"Hind",sans-serif;color:var(--ink);position:relative}
.masthead{position:absolute;left:0;top:0;width:1200px;height:63px;background:var(--brand);display:flex;align-items:center;justify-content:center}
.brand-name{color:#fff;font-family:"Cabin",sans-serif;font-weight:500;font-size:25px;letter-spacing:.5px}
.main-nav{position:absolute;left:0;top:63px;width:1200px;height:43px;background:var(--nav);font-family:"Cabin",sans-serif;font-size:14.5px;font-weight:500;color:#fff}
.main-nav a{position:absolute;top:0;height:43px;color:#fff;text-decoration:none;display:flex;align-items:center;justify-content:center;white-space:nowrap}
.main-nav .sep{position:absolute;top:7px;width:1px;height:29px;background:#bbb}
.main-nav .active{background:var(--brand)}
.main-nav svg{margin-right:5px}
.nav-band{position:absolute;left:0;top:106px;width:1200px;height:11px;background:var(--brand)}
.content{position:absolute;left:62px;top:117px;width:1076px;height:758px;background:var(--panel)}
.hero{position:absolute;left:5px;top:6px;width:789px;height:494px}
.hero-photo{position:absolute;left:0;top:0;width:789px;height:443px;background:radial-gradient(ellipse at 20% 35%,#b8a58a 0%,#5d4d3e 30%,#221d1a 65%,#141210 100%)}
.credit{position:absolute;right:2px;top:4px;writing-mode:vertical-rl;color:#fff;font-size:7px;letter-spacing:.5px}
.arrow{position:absolute;top:205px}
.hero-caption{position:absolute;left:0;top:443px;width:789px;height:51px;background:var(--brand);color:#fff;font-weight:600;font-size:33px;line-height:51px;padding-left:8px;white-space:nowrap}
.wire{position:absolute;left:804px;top:6px;width:266px;height:494px}
.wire h2{font-family:"Cabin",sans-serif;font-weight:400;color:var(--brand);font-size:26px;margin:8px 0 0 5px;padding-bottom:10px;border-bottom:2px solid var(--brand);width:250px;line-height:30px}
.wire-list{position:absolute;left:0;top:65px;width:266px;height:428px;background:var(--wire-bg);overflow:hidden;padding:0 22px 0 12px}
.wire-list::after{content:"";position:absolute;right:4px;top:10px;width:4px;height:86px;background:#c8c8c8;border-radius:2px}
.wire-item{padding:18px 0 16px;border-bottom:1px solid #ddd}
.wire-time{color:var(--muted);font-size:15px;display:flex;align-items:center;gap:5px}
.wire-title{font-size:15.5px;font-weight:500;line-height:22px;margin-top:2px;letter-spacing:.35px}
.focus-bar{position:absolute;left:5px;top:508px;width:1065px;height:31px;background:#f1f1f1;font-weight:600;font-size:15.5px;line-height:33px;padding-left:9px}
.cards{position:absolute;left:7px;top:549px}
.card{position:absolute;width:247px}
.card-photo{height:139px}
.card-title{font-family:"Arimo",sans-serif;font-size:19px;line-height:23px;margin-top:6px;color:#222}
.site-footer{position:absolute;left:0;top:875px;width:1200px;height:125px;background:var(--footer);color:var(--footer-ink);text-align:center;font-family:"Cabin",sans-serif}
.footer-nav{display:flex;justify-content:center;gap:25px;font-size:17.5px;margin-top:11px;color:#333}
.legal{font-size:15.5px;color:#fff;line-height:18.5px;margin-top:11px}
.legal-links{font-size:15.5px;color:#fff;word-spacing:4px;line-height:18.5px}
</style>
</head>
<body>
<header class="masthead"><span class="brand-name">YOUR LOGO</span></header>
<nav class="main-nav">
  <a style="left:0;width:62px" href="#"><svg width="22" height="24" viewBox="0 0 22 24" style="margin:0"><path d="M11 2 1 11h3v8h5v-5h4v5h5v-8h3z" fill="#fff"/><rect x="1" y="21" width="20" height="2" fill="var(--brand)"/></svg></a>
  <a class="active" style="left:62px;width:98px" href="#">LAST MINUTE</a>
  <span class="sep" style="left:176px"></span>
  <a style="left:176px;width:99px" href="#">MARKETS</a>
  <span class="sep" style="left:275px"></span>
  <a style="left:275px;width:91px" href="#">WORLD</a>
  <span class="sep" style="left:366px"></span>
  <a style="left:366px;width:92px" href="#">POLITICS</a>
  <span class="sep" style="left:458px"></span>
  <a style="left:458px;width:71px" href="#">TECH</a>
  <span class="sep" style="left:529px"></span>
  <a style="left:529px;width:133px" href="#">COMMENTARY</a>
  <span class="sep" style="left:662px"></span>
  <a style="left:662px;width:153px" href="#">EXPERT ANGLES</a>
  <span class="sep" style="left:815px"></span>
  <a style="left:815px;width:86px" href="#">MONEY</a>
  <span class="sep" style="left:901px"></span>
  <a style="left:901px;width:65px" href="#">LIFE</a>
  <span class="sep" style="left:966px"></span>
  <a style="left:966px;width:102px" href="#"><svg width="13" height="11" viewBox="0 0 13 11"><rect x=".8" y=".8" width="11.4" height="9.4" fill="none" stroke="#fff" stroke-width="1.4"/><path d="M2 9l3-4 2 2.5 1.5-1.5L11 9z" fill="#fff"/></svg>PICTURES</a>
  <span class="sep" style="left:1068px"></span>
  <a style="left:1068px;width:80px" href="#"><svg width="16" height="11" viewBox="0 0 16 11"><rect x=".8" y=".8" width="10" height="9.4" fill="none" stroke="#fff" stroke-width="1.4"/><path d="M11 5.5l4-3v6z" fill="none" stroke="#fff" stroke-width="1.2"/></svg>VIDEO</a>
  <a style="left:1160px;width:26px" href="#"><svg width="15" height="14" viewBox="0 0 15 14" style="margin:0"><rect y="1" width="15" height="2.5" fill="#fff"/><rect y="6" width="15" height="2.5" fill="#fff"/><rect y="11" width="15" height="2.5" fill="#fff"/></svg></a>
</nav>
<div class="nav-band"></div>

<main class="content">
  <section class="hero">
    <div class="hero-photo" role="img" aria-label="Armed police officers in helmets on a night street"></div>
    <span class="credit">R. VALMONT/WIRE</span>
    <svg class="arrow" style="left:9px" width="62" height="62" viewBox="0 0 62 62"><path d="M2 31 30 3l8 8-14 14h36v12H24l14 14-8 8z" fill="#fff"/></svg>
    <svg class="arrow" style="left:713px" width="62" height="62" viewBox="0 0 62 62"><path d="M60 31 32 3l-8 8 14 14H2v12h36L24 51l8 8z" fill="#fff"/></svg>
    <h1 class="hero-caption">Le Roy demands closure of all Islamist mosques</h1>
  </section>

  <aside class="wire">
    <h2>THE WIRE</h2>
    <div class="wire-list">
      <article class="wire-item"><div class="wire-time"><svg width="11" height="11" viewBox="0 0 11 11"><circle cx="5.5" cy="5.5" r="4.6" fill="none" stroke="#888" stroke-width="1.2"/><path d="M5.5 3v2.8h2" fill="none" stroke="#888" stroke-width="1.2"/></svg>13m ago</div><p class="wire-title">Death toll in Afghan base attack rises to 140, officials say</p></article>
      <article class="wire-item"><div class="wire-time"><svg width="11" height="11" viewBox="0 0 11 11"><circle cx="5.5" cy="5.5" r="4.6" fill="none" stroke="#888" stroke-width="1.2"/><path d="M5.5 3v2.8h2" fill="none" stroke="#888" stroke-width="1.2"/></svg>20m ago</div><p class="wire-title">Islamic State-linked Kalantar leader killed on Philippine resort island: army</p></article>
      <article class="wire-item"><div class="wire-time"><svg width="11" height="11" viewBox="0 0 11 11"><circle cx="5.5" cy="5.5" r="4.6" fill="none" stroke="#888" stroke-width="1.2"/><path d="M5.5 3v2.8h2" fill="none" stroke="#888" stroke-width="1.2"/></svg>48m ago</div><p class="wire-title">Thousands of ex-Taliban fighters may have entered Germany: report</p></article>
      <article class="wire-item"><div class="wire-time"><svg width="11" height="11" viewBox="0 0 11 11"><circle cx="5.5" cy="5.5" r="4.6" fill="none" stroke="#888" stroke-width="1.2"/><path d="M5.5 3v2.8h2" fill="none" stroke="#888" stroke-width="1.2"/></svg>1h ago</div><p class="wire-title">Peaceful outcome for Korean nuclear standoff possible, envoy says</p></article>
    </div>
  </aside>

  <div class="focus-bar">French election in focus</div>

  <section class="cards">
    <article class="card" style="left:0"><div class="card-photo" role="img" aria-label="Two candidates speaking at rallies before a French flag" style="background:linear-gradient(90deg,#2f4a8a 0%,#c9c4c2 45%,#b5302c 100%)"></div><p class="card-title">The election 'nightmare' that could smash the euro</p></article>
    <article class="card" style="left:272px"><div class="card-photo" role="img" aria-label="Illustrated guide with candidate portraits and flag icons" style="background:linear-gradient(180deg,#a9d8d9 0%,#9fd0d2 70%,#c9c07a 100%)"></div><p class="card-title">The beginner's guide to the French elections</p></article>
    <article class="card" style="left:542px"><div class="card-photo" role="img" aria-label="Candidate greeting a crowd waving French flags" style="background:linear-gradient(180deg,#8fa3c4 0%,#d9d6dc 50%,#c0404a 100%)"></div><p class="card-title">Opinion: Win or lose, Le Roy is a nightmare for EU</p></article>
    <article class="card" style="left:814px"><div class="card-photo" role="img" aria-label="Collage of European politicians on a blue and yellow background" style="background:linear-gradient(180deg,#2c7fc4 0%,#7fa8b8 50%,#c9c9c9 100%)"></div><p class="card-title">What's wrong with Europe?</p></article>
  </section>
</main>

<footer class="site-footer">
  <nav class="footer-nav"><span>Regions</span><span>MONEY</span><span>ENTERTAINMENT</span><span>TECH</span><span style="margin-left:12px">SPORT</span><span>TRAVEL</span><span style="margin-left:-8px">HEALTH</span><span>FEATURES</span></nav>
  <p class="legal">© 2017 YourCompany Meridian Broadcasting Group, Inc. All Rights Reserved.<br>YourCompany ™ &amp; © 2016 YourCompany</p>
  <p class="legal-links">Terms of UsePrivacy Policy AdChoices Advertise with us About us Newsletters Work for us Help Transcripts License Footage YourCompany.</p>
</footer>
</body>
</html>
```